Business card design for strategy and management consulting company. Would like to have a clean and professional business card, based on the attached logo. The company is a strategy and management consulting company focusing on sustainable business modlels based on economic, social and environmental market opportunities. Preferably the logo should be included on both sides of the design.

Industry/Entity Type

Business

Contact Information for Business Card

Håvard Lilleby, CEO/Management consultant
havard.lilleby@quarvenpartners.example
Mob: +47 948 26 317
Office: Vikfjell gate 14, pb 312 sentrum, N-0172 Oslo Norway

Requirements
Must have
• Include attached logo
Nice to have
• Would like to have the logo on both sides
Should not have
• Many colours.

```html
<!DOCTYPE html>
<html lang="en">
<head>
<meta charset="utf-8">
<title>Quarven – Business Card</title>
<link rel="stylesheet" href="https://fonts.googleapis.com/css2?family=Open+Sans:wght@400;600&display=swap">
<style>
  :root {
    --page-bg: #d9d9d6;
    --card-face: #f1f1ef;
    --ink: #000000;
    --paper-text: #ffffff;
  }
  html, body {
    margin: 0;
    width: 1200px;
    height: 900px;
    overflow: hidden;
    background: var(--page-bg);
  }
  .card {
    position: absolute;
    left: 160px;
    top: 178px;
    width: 880px;
    height: 545px;
    display: block;
  }
  .card__face { fill: var(--card-face); }
  .card__band { fill: var(--ink); }
  .card__ring { fill: var(--card-face); stroke: var(--ink); stroke-width: 6; }
  .holder-name {
    font-family: "Open Sans", sans-serif;
    font-size: 25px;
    font-weight: 400;
    fill: var(--paper-text);
  }
  .holder-title {
    font-family: "Open Sans", sans-serif;
    font-size: 16px;
    font-weight: 400;
    fill: var(--paper-text);
  }
  .contact-line {
    font-family: "Open Sans", sans-serif;
    font-size: 13px;
    font-weight: 400;
    fill: var(--paper-text);
  }
  .contact-icon { fill: var(--paper-text); }
  .contact-icon--stroke { fill: none; stroke: var(--paper-text); stroke-width: 1.6; stroke-linecap: round; }
  .brand-name {
    font-family: "Open Sans", sans-serif;
    font-size: 74px;
    font-weight: 600;
    fill: var(--ink);
    letter-spacing: -1px;
  }
</style>
</head>
<body>
  <svg class="card" viewBox="0 0 670 415" role="group" aria-label="Quarven business card, front">
    <defs>
      <clipPath id="card-outline">
        <path d="M0 0 H462 A206.5 206.5 0 0 1 462 413 H0 Z"/>
      </clipPath>
    </defs>

    <g clip-path="url(#card-outline)">
      <path class="card__face" d="M0 0 H462 A206.5 206.5 0 0 1 462 413 H0 Z"/>
      <rect class="card__band card__band--top" x="0" y="0" width="670" height="115"/>
      <rect class="card__band card__band--bottom" x="0" y="293" width="670" height="122"/>
    </g>

    <circle class="card__ring" cx="462" cy="206.5" r="203.5"/>

    <g class="holder">
      <text class="holder-name" x="32" y="60">Håvard Lilleby</text>
      <text class="holder-title" x="32" y="85">Managing Director</text>
    </g>

    <g class="contacts">
      <g class="contact contact--phone">
        <path class="contact-icon" d="M35 320.5c1-1 2-1 2.6-.3l1.6 2c.5.6.4 1.4-.2 1.9l-.9.8c.7 1.6 2 2.9 3.6 3.6l.8-.9c.5-.6 1.3-.7 1.9-.2l2 1.6c.7.6.7 1.6-.3 2.6-1 1-2.6 1.3-4.4.4-3.3-1.6-5.8-4.1-7.4-7.4-.9-1.8-.6-3.4.4-4.4z"/>
        <text class="contact-line" x="57" y="331">+47 948 26 317</text>
      </g>
      <g class="contact contact--web">
        <path class="contact-icon--stroke" d="M39 352.5l4-4M37.5 350.5l-1.5 1.5a2.6 2.6 0 0 0 3.7 3.7l1.5-1.5M44.5 354.5l1.5-1.5a2.6 2.6 0 0 0-3.7-3.7l-1.5 1.5"/>
        <text class="contact-line" x="57" y="355">www.quarvenpartners.example</text>
      </g>
      <g class="contact contact--email">
        <rect class="contact-icon" x="34" y="370" width="13" height="9" rx="1"/>
        <path d="M34.6 370.8l5.9 4.6 5.9-4.6" fill="none" stroke="#000" stroke-width="1.2"/>
        <text class="contact-line" x="57" y="379">havard.lilleby@quarvenpartners.example</text>
      </g>
    </g>

    <text class="brand-name" x="436" y="234" text-anchor="middle">Quarven</text>
  </svg>
</body>
</html>
```